Geschäftspapiere für familiengeführtes Zeitarbeitsunternehmen
Zielgruppe
Wir sind ein familiengeführtes Zeitarbeitsunternehmen. Somit haben wir 2 Zielgruppen, unsere Kunden und unsere Mitarbeiter. Eine Übersicht von uns findet man am besten auf unserer Website www.brandt-kraefte.de
Aufgabenstellung
Wir möchten 'nur' angepasstes Briefpapier mit neuen Daten. Gerne können Sie uns auch Vorschläge bezüglich eines verbesserten Designs machen.
Folgende Änderungen sind zu verarbeiten:
- die Geschäftstellen in Neustadt und Zell wurde geschlossen, daher ist Oberhof nun Hauptgeschäftsstelle
- die Firmierung hat sich geändert: das pw wurde entfernt
- Plaudernetz und bildoria kann raus
- Neu: UID DE 31 47 26 804
- Neu: Amtgericht Jena HRB 742391
- Neu rein bitte noch: Hinweis zum Datenschutz: https://brandt-kraefte.de/datenschutz/

```html
<!DOCTYPE html>
<html lang="de">
<head>
<meta charset="utf-8">
<title>Briefpapier – Brandt Kräfte GmbH</title>
<link rel="stylesheet" href="https://fonts.googleapis.com/css2?family=Roboto:wght@300;400;700&display=swap">
<style>
  :root {
    --brand-blue: #0381ad;
    --text-grey: #6f6f6f;
    --paper-top: #ffffff;
    --paper-bottom: #e6e6e6;
    --white: #ffffff;
  }
  * { margin: 0; padding: 0; box-sizing: border-box; }
  html, body { width: 848px; height: 1200px; overflow: hidden; }
  body { font-family: "Roboto", Arial, sans-serif; color: var(--text-grey); }

  .letterhead {
    position: relative;
    width: 848px;
    height: 1200px;
    background: linear-gradient(180deg, var(--paper-top) 0%, #fafafa 40%, var(--paper-bottom) 100%);
    overflow: hidden;
  }

  .top-band {
    position: absolute; left: 0; top: 0;
    width: 100%; height: 44px;
    background: var(--brand-blue);
  }
  .top-band__url {
    position: absolute; right: 40px; top: 13px;
    font-size: 15px; font-weight: 700; color: var(--white);
    letter-spacing: 0.1px;
  }

  .brand-name {
    position: absolute; right: 40px; top: 104px;
    display: flex; align-items: center; gap: 12px;
    color: var(--brand-blue); font-weight: 700;
  }
  .brand-name__dot {
    width: 22px; height: 22px; border-radius: 50%;
    background: var(--brand-blue);
  }
  .brand-name__text {
    font-size: 44px; line-height: 1; letter-spacing: 3px;
    text-align: right;
  }
  .brand-name__text span { display: block; font-size: 28px; letter-spacing: 7px; margin-top: 8px; }

  .sender-line {
    position: absolute; left: 81px; top: 197px;
    font-size: 11px; font-weight: 300;
  }

  .info-block {
    position: absolute; left: 648px;
    font-size: 12.5px; font-weight: 300; line-height: 24.2px;
    list-style: none;
  }
  .info-block--contact { top: 263px; }
  .info-block--legal { top: 1046px; }

  .privacy-note {
    position: absolute; left: 81px; top: 1146px;
    font-size: 11px; font-weight: 300;
  }
</style>
</head>
<body>
  <main class="letterhead">
    <header class="top-band">
      <span class="top-band__url">www.brandt-kraefte.de</span>
    </header>

    <div class="brand-name" aria-label="Brandt Kräfte">
      <div class="brand-name__dot"></div>
      <div class="brand-name__text">BRANDT<span>KRÄFTE</span></div>
    </div>

    <p class="sender-line">Brandt Kräfte GmbH · Lindenhofer Straße 2 · D-98571 Tannberg</p>

    <ul class="info-block info-block--contact">
      <li>Brandt Kräfte GmbH</li>
      <li>Lindenhofer Straße 2</li>
      <li>D-98571 Tannberg</li>
      <li>Tel: +49 36847 412 360</li>
      <li>Fax: +49 36847 412 369</li>
      <li>kontakt@brandt-kraefte.de</li>
    </ul>

    <ul class="info-block info-block--legal">
      <li>Geschäftsführer:</li>
      <li>Marlo Theo Brandt</li>
      <li>UID: DE 31 47 26 804</li>
      <li>Amtsgericht Jena</li>
      <li>HRB 742391</li>
    </ul>

    <p class="privacy-note">Hinweis zum Datenschutz: https://brandt-kraefte.de/datenschutz/</p>
  </main>
</body>
</html>
```